WWW.VELTRONA.IT BUSINNES CARD

WE NEED A BUSINESS CARD . I HAVE A COMPANY IN ITALY NR 1 IN HAIR MEDICAL CARE AN HAIR REPLECEMENT . IN CARD I NEED WRITE WEB ADDRESS, MAIL , ADDRESS, TELEPHONE NUMBER , AND NAME
IN THE BACK SIDE I NEED MY DOCTOR LOGO .
MY WEB SITE IS WWW.VELTRONA.IT
Updates

Target Market(s)

CONSUMER B2C

Industry/Entity Type

Hair And Beauty

Contact Information for Business Card

I WANT A MEDICAL BUSINESS CARD.

Font styles to use
Other font styles liked:
• VERDANA

Colors
33a6d7
3176b5
85abd2
aedbee
eaf1f7
ffffff

Requirements
Must have
• I NEED MY LOGO AND LOGO OF DR VELTRONA

```html
<!DOCTYPE html>
<html lang="it">
<head>
<meta charset="utf-8">
<title>Veltrona – Business Card</title>
<link rel="stylesheet" href="https://fonts.googleapis.com/css2?family=Arimo:wght@400;700&display=swap">
<style>
  :root {
    --sky: #33a6d7;
    --blue: #3176b5;
    --navy: #1f5a9e;
    --mist: #85abd2;
    --ice: #aedbee;
    --frost: #eaf1f7;
    --white: #ffffff;
    --ink: #1b2a3a;
    --grey: #555b62;
    --stage: #2c2c2e;
    --hair-dark: #6b3a1c;
    --hair-light: #c98a5e;
  }
  * { box-sizing: border-box; margin: 0; padding: 0; }
  html, body { width: 1200px; height: 997px; overflow: hidden; }
  body {
    background: var(--stage);
    font-family: "Arimo", Verdana, sans-serif;
    position: relative;
  }

  .card {
    position: absolute;
    background: var(--white);
    box-shadow: 0 10px 30px rgba(0,0,0,.45);
    overflow: hidden;
  }
  .card svg.card-art { position: absolute; inset: 0; }

  /* Back side */
  .card-back { left: 110px; top: 238px; width: 300px; height: 520px; }
  .back-web {
    position: absolute; right: 3px; top: 280px;
    transform: rotate(90deg); transform-origin: right top;
    color: var(--white); font-size: 11px; font-weight: 700; letter-spacing: .3px;
    white-space: nowrap;
  }
  .doctor-name {
    position: absolute; left: 40px; top: 70px;
    color: var(--navy); font-size: 30px; font-weight: 700;
  }
  .mascot {
    position: absolute; left: 40px; top: 125px; width: 200px; height: 340px;
    border-radius: 50% 50% 46% 46% / 30% 30% 20% 20%;
    background: radial-gradient(ellipse at 50% 40%, var(--hair-light), var(--hair-dark) 55%, var(--frost) 100%);
    opacity: .85;
  }

  /* Front side */
  .card-front { left: 460px; top: 348px; width: 630px; height: 360px; }
  .brand {
    position: absolute; left: 150px; top: 62px;
    display: flex; align-items: center; gap: 12px;
  }
  .brand-mark { width: 30px; height: 30px; background: var(--sky); }
  .brand-name { color: var(--navy); font-size: 44px; font-weight: 700; }
  .tagline {
    position: absolute; left: 150px; top: 118px;
    color: var(--blue); font-size: 13px; letter-spacing: .6px;
    white-space: nowrap;
  }
  .person { position: absolute; left: 34px; top: 196px; }
  .person-name { color: var(--navy); font-size: 15px; font-weight: 700; }
  .person-role { color: var(--grey); font-size: 14px; margin-top: 3px; }
  .contacts { position: absolute; left: 34px; top: 248px; list-style: none; }
  .contacts li {
    display: flex; align-items: center; gap: 12px;
    color: var(--ink); font-size: 14px; height: 22px;
  }
  .contacts svg { width: 16px; height: 16px; }
  .address {
    position: absolute; right: 30px; top: 226px; text-align: right;
    color: var(--sky); font-size: 13px; line-height: 17px;
  }
  .front-web {
    position: absolute; right: 26px; top: 300px;
    color: var(--white); font-size: 15px; font-weight: 700;
  }
</style>
</head>
<body>

<section class="card card-back" aria-label="Back side">
  <svg class="card-art" viewBox="0 0 300 520" aria-hidden="true">
    <path d="M0 10 H250 Q268 10 268 28 V520" fill="none" stroke="var(--ice)" stroke-width="6"/>
    <path d="M272 30 Q272 14 288 14 H300 V520 H272 Z" fill="var(--navy)"/>
  </svg>
  <div class="back-web">www.veltrona.it</div>
  <div class="doctor-name">dr. Veltrona</div>
  <div class="mascot" role="img" aria-label="Mascot illustration: cartoon hair-strand doctor in a white coat giving a thumbs up"></div>
</section>

<section class="card card-front" aria-label="Front side">
  <svg class="card-art" viewBox="0 0 630 360" aria-hidden="true">
    <line x1="440" y1="88" x2="600" y2="88" stroke="var(--ink)" stroke-width="1"/>
    <line x1="230" y1="205" x2="600" y2="205" stroke="var(--ink)" stroke-width="1"/>
    <path d="M0 330 H300 Q318 330 322 320" fill="none" stroke="var(--sky)" stroke-width="8"/>
    <path d="M340 312 Q346 288 372 288 H630 V360 H300 Q330 350 340 312 Z" fill="var(--navy)"/>
    <rect x="0" y="342" width="630" height="6" fill="var(--ice)"/>
    <rect x="0" y="350" width="630" height="10" fill="var(--navy)"/>
  </svg>

  <div class="brand">
    <span class="brand-mark"></span>
    <span class="brand-name">VELTRONA</span>
  </div>
  <div class="tagline">CURA E REINTEGRAZIONE DEI CAPELLI</div>

  <div class="person">
    <div class="person-name">Mrs Elena Moravi</div>
    <div class="person-role">Director</div>
  </div>

  <ul class="contacts">
    <li>
      <svg viewBox="0 0 16 16"><circle cx="8" cy="8" r="8" fill="var(--navy)"/><path d="M4 9h8v3H4z M5 6h6l1 3H4z" fill="var(--white)"/></svg>
      02 5550 1842
    </li>
    <li>
      <svg viewBox="0 0 16 16"><circle cx="8" cy="8" r="8" fill="var(--navy)"/><rect x="5.5" y="3.5" width="5" height="9" rx="1" fill="none" stroke="var(--white)" stroke-width="1.2"/></svg>
      0400 555 317
    </li>
    <li>
      <svg viewBox="0 0 16 16"><circle cx="8" cy="8" r="8" fill="var(--navy)"/><rect x="4" y="5" width="8" height="6" fill="none" stroke="var(--white)" stroke-width="1.1"/><path d="M4 5l4 3.5L12 5" fill="none" stroke="var(--white)" stroke-width="1.1"/></svg>
      elena@veltrona.it
    </li>
  </ul>

  <div class="address">Suite 4.12 28 Orchard Lane<br>Bellmora NSW 2099</div>
  <div class="front-web">www.veltrona.it</div>
</section>

</body>
</html>
```